School Poster

Design so that these can be placed in classrooms across the school.

Attached is another design we have had done. Use a similar theme.

Consider using themes from https://tolvanehs.qx.edu.au/

please edit Binder1 doc.

Target Market(s)

Students and teachers

```html
<!DOCTYPE html>
<html lang="en">
<head>
<meta charset="utf-8">
<title>Tolvane SHS Classroom Posters</title>
<link rel="stylesheet" href="https://fonts.googleapis.com/css2?family=Montserrat:wght@500;600;700;800;900&display=swap">
<style>
:root{
  --stage:#555555;
  --navy:#0d2a6b;
  --blue:#1565c0;
  --gold:#f2b705;
  --yellow:#f7c600;
  --card-a:#fcd65a;
  --card-b:#f7e27c;
  --paper:#f6f6f8;
  --red:#e53935;
  --white:#ffffff;
}
*{box-sizing:border-box;margin:0;padding:0}
html,body{width:1200px;height:858px;overflow:hidden;background:var(--stage);font-family:"Montserrat",sans-serif}
.poster{position:absolute;top:96px;width:470px;height:666px;background:var(--paper);overflow:hidden}
.poster--help{left:84px}
.poster--ai{left:646px}
.abs{position:absolute}
.bg{position:absolute;left:0;top:0}

/* help poster */
.gold-rail{left:0;top:0;width:14px;height:250px;background:var(--gold)}
.help-title{left:32px;top:32px;font-weight:900;color:var(--navy);font-size:29px;line-height:26px;letter-spacing:-.3px}
.help-sub{left:33px;top:84px;font-weight:800;color:var(--yellow);font-size:20px}
.school-mark{display:flex;align-items:center;gap:6px;font-weight:800;color:var(--navy);font-size:13px;line-height:15px}
.school-mark .dot{width:14px;height:14px;background:var(--navy)}
.help-mark{left:360px;top:62px}
.pill{background:var(--blue);color:var(--white);font-weight:700;font-size:8.6px;border-radius:12px 12px 12px 0;padding:0 10px 0 18px;display:flex;flex-direction:column;justify-content:center;line-height:9.6px;white-space:nowrap}
.step-num{z-index:2;width:24px;height:24px;border-radius:50%;background:var(--white);border:2px solid var(--gold);color:var(--navy);font-weight:800;font-size:10px;display:flex;align-items:center;justify-content:center}
.ticks{list-style:none;font-size:7px;font-weight:500;color:var(--navy);line-height:10.4px}
.ticks li{display:flex;align-items:center;gap:4px}
.ticks li::before{content:"";width:5px;height:5px;border-radius:50%;background:var(--blue);flex:none}
.step-label{position:absolute;left:0;width:100%;text-align:center;font-weight:700;font-size:10px;color:var(--navy);line-height:11px}
.icon-slot{position:absolute;border-radius:8px}
.motto{left:34px;top:536px;color:var(--white);font-weight:900}
.motto .we{font-size:21px;line-height:26px}
.motto .word{display:block;margin-top:5px;background:var(--yellow);color:var(--navy);font-size:16px;padding:1px 4px;width:80px;line-height:19px}
.refs{left:126px;top:582px;width:330px;color:var(--white);font-size:5.4px;font-weight:700;line-height:7px;text-transform:uppercase}
.refs p+p{margin-top:7px}

/* ai poster */
.ai-band{left:98px;top:44px;width:338px;height:66px;background:var(--navy);border-radius:0 8px 8px 0}
.ai-title{left:124px;top:50px;font-weight:800;font-size:27px;line-height:27px;color:var(--white)}
.ai-title span{color:var(--yellow)}
.ai-mark{left:30px;top:56px;width:82px;height:58px;background:var(--white);border-radius:6px;padding:0 6px}
.mid-band{left:0;top:208px;width:470px;height:184px;background:var(--navy)}
.foot-band{left:0;top:556px;width:470px;height:110px;background:var(--card-a)}
.tab{background:var(--blue);color:var(--white);font-weight:700;font-size:17px;border-radius:12px 12px 0 0;display:flex;align-items:center;justify-content:center}
.rule-box{background:var(--white);border:2px solid var(--blue);border-radius:10px;display:grid;grid-template-columns:71px 114px 92px 1fr;padding:10px 8px 0;gap:0}
.rule-box p{font-size:9.8px;font-weight:500;color:var(--navy);line-height:11.8px;padding-left:12px;position:relative}
.rule-box p::before{content:"";position:absolute;left:0;top:2px;width:8px;height:8px;border-radius:50%;background:var(--blue)}
.rule-box.cannot p::before{background:var(--red)}
.help-head{left:34px;top:272px;color:var(--white);font-weight:700;font-size:17px;line-height:22px}
.help-head span{color:var(--yellow)}
.head-rule{left:188px;top:314px;width:248px;height:1px;background:rgba(255,255,255,.5)}
.card{top:356px;width:94px;height:80px;border:2px solid var(--navy);border-radius:6px;text-align:center;color:var(--blue);font-weight:600;font-size:10px;line-height:12px;padding:18px 4px 0}
.card--deep{background:var(--card-a)}
.card--soft{background:var(--card-b)}
.card-tick{position:absolute;top:-12px;left:35px;width:24px;height:24px}
.closing{left:0;top:600px;width:470px;text-align:center;font-weight:700;font-size:14px;line-height:18px;color:var(--navy)}
.closing span{color:var(--blue)}
</style>
</head>
<body>

<section class="poster poster--help">
  <svg class="bg" width="470" height="666" viewBox="0 0 470 666">
    <path d="M0 300 C110 300 210 400 300 470 C360 512 420 520 470 500 L470 666 L0 666 Z" fill="#0d2a6b"/>
    <path d="M230 666 C280 560 400 520 470 540 L470 666 Z" fill="#143a8a"/>
    <path d="M64 262 L64 325 L178 325 L178 436 L282 436 L282 488" fill="none" stroke="#c99600" stroke-width="12"/>
    <line x1="62" y1="160" x2="62" y2="200" stroke="#0d2a6b" stroke-width="1"/>
    <line x1="158" y1="246" x2="158" y2="310" stroke="#0d2a6b" stroke-width="1"/>
    <line x1="264" y1="362" x2="264" y2="424" stroke="#0d2a6b" stroke-width="1"/>
    <circle cx="64" cy="262" r="58" fill="#fff" stroke="#f2b705" stroke-width="13"/>
    <circle cx="178" cy="374" r="58" fill="#fff" stroke="#f2b705" stroke-width="13"/>
    <circle cx="282" cy="488" r="58" fill="#fff" stroke="#f2b705" stroke-width="13"/>
  </svg>
  <div class="abs gold-rail"></div>

  <h1 class="abs help-title">BEFORE YOU ASK<br>THE TEACHER...</h1>
  <p class="abs help-sub">TRY THESE STEPS FIRST!</p>
  <div class="abs school-mark help-mark"><span class="dot"></span>Tolvane<br>SHS</div>

  <div class="abs pill" style="left:64px;top:126px;width:172px;height:24px">Don't give up straight away</div>
  <div class="abs step-num" style="left:50px;top:136px">01</div>
  <ul class="abs ticks" style="left:82px;top:154px">
    <li>Read the question carefully.</li>
    <li>Identify what you already know.</li>
    <li>Try a strategy you've used before.</li>
    <li>Give yourself thinking time.</li>
  </ul>

  <div class="abs pill" style="left:160px;top:212px;width:186px;height:24px">Before asking for help chock</div>
  <div class="abs step-num" style="left:146px;top:222px">02</div>
  <ul class="abs ticks" style="left:178px;top:241px">
    <li>Learning goal andsuccess criteria.</li>
    <li>Worked examples.</li>
    <li>Class notes.</li>
    <li>Classroom displays.</li>
    <li>ClassHub resources.</li>
    <li>Task sheet and instructions.</li>
  </ul>

  <div class="abs pill" style="left:266px;top:328px;width:166px;height:24px"><span>Ask three sources before</span><span>asking the teacher</span></div>
  <div class="abs step-num" style="left:252px;top:338px">03</div>
  <ul class="abs ticks" style="left:284px;top:357px">
    <li>A person (partner or neighbour)</li>
    <li>A place (notes, display, ClassHub)</li>
    <li>A resource (worked example, task sheet)</li>
  </ul>

  <div class="abs" style="left:6px;top:204px;width:116px;height:116px">
    <div class="icon-slot" role="img" aria-label="Head with gear icon" style="left:42px;top:20px;width:32px;height:34px;background:var(--blue)"></div>
    <p class="step-label" style="top:64px">THINK FIRST</p>
  </div>
  <div class="abs" style="left:120px;top:316px;width:116px;height:116px">
    <div class="icon-slot" role="img" aria-label="Document with tick icon" style="left:44px;top:18px;width:28px;height:36px;background:var(--blue)"></div>
    <p class="step-label" style="top:64px">CHECK YOUR<br>SUPPORTS</p>
  </div>
  <div class="abs" style="left:224px;top:430px;width:116px;height:116px">
    <div class="icon-slot" role="img" aria-label="Group of people asking for help icon" style="left:38px;top:20px;width:40px;height:32px;background:var(--blue)"></div>
    <p class="step-label" style="top:64px">ASK 3<br>BEFORE ME</p>
  </div>

  <div class="abs motto">
    <div class="we">WE</div>
    <span class="word">BELIEVE</span>
    <span class="word">STRIVE</span>
    <span class="word">ACHIEVE</span>
  </div>
  <div class="abs refs">
    <p>Hollis, M. 2025. "Why students don't ask for help- and how to change that" downloaded on 24/04/2026 from https://www.learnwise.org/article/getting-students-ask-help/</p>
    <p>SRI, 2024. "Supporting self-regulated learning", downloaded on 24/04/2026 from https://www.schoolinsight.edu.au/files/2024-02/supporting-self-regulated-learning.pdf</p>
  </div>
</section>

<section class="poster poster--ai">
  <div class="abs mid-band"></div>
  <div class="abs foot-band"></div>

  <div class="abs ai-band"></div>
  <h1 class="abs ai-title">USING AI &amp; OTHER<br><span>TOOLS RESPONSIBLY</span></h1>
  <div class="abs school-mark ai-mark"><span class="dot"></span>Tolvane<br>SHS</div>

  <div class="abs tab" style="left:126px;top:142px;width:218px;height:32px">What You Must Do</div>
  <div class="abs rule-box" style="left:34px;top:173px;width:402px;height:84px">
    <p>Complete your own work</p>
    <p>Demonstrate your progress (drafts, notes,planning, revisions)</p>
    <p>Use feedback to improve your work</p>
    <p>Demonstrate your understanding of the ideas in your submission</p>
  </div>

  <h2 class="abs help-head"><span>What AI can help you do</span> (when approved<br>by your teacher)</h2>
  <div class="abs head-rule"></div>

  <div class="abs card card--deep" style="left:32px">
    <svg class="card-tick" viewBox="0 0 24 24"><circle cx="12" cy="12" r="10.5" fill="#fff" stroke="#0d2a6b" stroke-width="2"/><path d="M7.5 12.3l3 3 6-6.2" fill="none" stroke="#0d2a6b" stroke-width="2.2" stroke-linecap="round" stroke-linejoin="round"/></svg>
    Brainstorm ideas</div>
  <div class="abs card card--soft" style="left:136px">
    <svg class="card-tick" viewBox="0 0 24 24"><circle cx="12" cy="12" r="10.5" fill="#fff" stroke="#0d2a6b" stroke-width="2"/><path d="M7.5 12.3l3 3 6-6.2" fill="none" stroke="#0d2a6b" stroke-width="2.2" stroke-linecap="round" stroke-linejoin="round"/></svg>
    Check spelling, grammar &amp; clarity</div>
  <div class="abs card card--deep" style="left:240px">
    <svg class="card-tick" viewBox="0 0 24 24"><circle cx="12" cy="12" r="10.5" fill="#fff" stroke="#0d2a6b" stroke-width="2"/><path d="M7.5 12.3l3 3 6-6.2" fill="none" stroke="#0d2a6b" stroke-width="2.2" stroke-linecap="round" stroke-linejoin="round"/></svg>
    Read your work aloud using text-to-speech tools</div>
  <div class="abs card card--soft" style="left:344px">
    <svg class="card-tick" viewBox="0 0 24 24"><circle cx="12" cy="12" r="10.5" fill="#fff" stroke="#0d2a6b" stroke-width="2"/><path d="M7.5 12.3l3 3 6-6.2" fill="none" stroke="#0d2a6b" stroke-width="2.2" stroke-linecap="round" stroke-linejoin="round"/></svg>
    Help identify areas for improvement in a draft</div>

  <div class="abs tab" style="left:126px;top:462px;width:218px;height:32px">What You Cannot Do</div>
  <div class="abs rule-box cannot" style="left:34px;top:493px;width:402px;height:85px">
    <p>Submit AI generated work as your own</p>
    <p>Copy &amp; paste AI responses without acknowledging or adapting them</p>
    <p>Use AI tools to complete thewhole task for you</p>
    <p>Submit work that does not demonstrate your understanding</p>
  </div>

  <p class="abs closing">If you didn't create, develop and understand it,<br><span>it isn't your work.</span></p>
</section>

</body>
</html>
```